ARC VOLLEY Business Card Project

I'd like to request a business card design for the new company I've launched.
The name of the company is "ARC VOLLEY" an indoor unmanned tennis practice facility.
We would like to see designs that use our brand identity color in the logo I've attached.
We hope to get the design with modern, luxurious and elegant tone and manner.
We hope the logo should not be too big.

Business card must have elements as below:
- Logo (One of the logos I've attached)
- Name (In Korean Text) : 박 서 윤
- Title (In Korean Text) : 대표
- Phone Number : 010-8472-3916
- Email Address : seoyun.park@arcvolley-example.co.kr
- Website : www.arcvolley-example.co.kr
- Instagram : arcvolley
- Address (In Korean text) : 경기도 용인시 수지구 풍덕천로 456 미래타워 5층 501호, 502호

Target Market(s)

Tennis amateurs in 20 to 40s

Industry/Entity Type

Sports, Hobby

Contact Information for Business Card

- Logo (One of the logos I've attached) - Name (In Korean Text) : 박 서 윤 - Title (In Korean Text) : 대표 - Phone Number : 010-8472-3916 - Email Address : seoyun.park@arcvolley-example.co.kr - Website : www.arcvolley-example.co.kr - Instagram : arcvolley - Address (In Korean text) : 경기도 용인시 수지구 풍덕천로 456 미래타워 5층 501호, 502호

Font styles to use
Sans Serif

Requirements
Must have
• Double sided
Nice to have
• Logo with intaglio or relief embossing
Should not have
• Logo should not be too big.

```html
<!DOCTYPE html>
<html lang="ko">
<head>
<meta charset="utf-8">
<title>ARC VOLLEY Business Card</title>
<link rel="stylesheet" href="https://fonts.googleapis.com/css2?family=Montserrat:wght@400;500;600&family=Noto+Sans+KR:wght@400;500&display=swap">
<style>
  :root {
    --brand-green: #2c4f37;
    --card-white: #ffffff;
    --ink: #2a2a2a;
    --faint: #f0f0f0;
    --backdrop: #e9e4dc;
  }
  * { margin: 0; padding: 0; box-sizing: border-box; }
  html, body { width: 900px; height: 1200px; overflow: hidden; }
  body {
    position: relative;
    background: var(--backdrop);
    font-family: "Montserrat", "Noto Sans KR", sans-serif;
  }
  .card {
    position: absolute;
    left: 80px;
    width: 742px;
    height: 440px;
    border-radius: 32px;
    overflow: hidden;
  }
  .card-front { top: 132px; background: var(--card-white); }
  .card-back { top: 638px; background: var(--brand-green); }

  .front-watermark { position: absolute; left: 465px; top: 8px; }

  .brand-lockup {
    position: absolute;
    left: 38px;
    top: 40px;
    display: flex;
    align-items: center;
    gap: 16px;
  }
  .brand-name {
    font-family: "Montserrat", sans-serif;
    font-weight: 600;
    font-size: 36px;
    letter-spacing: 1px;
    color: var(--brand-green);
  }

  .person { position: absolute; left: 38px; top: 186px; }
  .person-name {
    font-family: "Noto Sans KR", sans-serif;
    font-weight: 500;
    font-size: 26px;
    line-height: 34px;
    color: var(--brand-green);
    letter-spacing: 2px;
  }
  .person-title {
    font-family: "Noto Sans KR", sans-serif;
    font-size: 13px;
    color: var(--ink);
    margin-top: 2px;
  }
  .divider {
    position: absolute;
    left: 38px;
    top: 252px;
    width: 668px;
    height: 1.5px;
    background: var(--brand-green);
  }
  .contact-list {
    position: absolute;
    left: 38px;
    top: 262px;
    list-style: none;
  }
  .contact-item {
    display: flex;
    align-items: center;
    gap: 10px;
    font-size: 15.5px;
    color: var(--ink);
    height: 24px;
    white-space: nowrap;
  }
  .contact-item.address { font-family: "Noto Sans KR", sans-serif; font-size: 14.5px; }
  .contact-item svg { width: 14px; height: 14px; fill: var(--brand-green); flex: none; }

  .back-lockup {
    position: absolute;
    left: 0; right: 0;
    top: 90px;
    display: flex;
    flex-direction: column;
    align-items: center;
    gap: 34px;
  }
  .back-lockup .brand-name {
    color: var(--card-white);
    font-size: 58px;
    letter-spacing: 2px;
  }
</style>
</head>
<body>
  <section class="card card-front">
    <svg class="front-watermark" width="320" height="320" viewBox="0 0 320 320" aria-hidden="true">
      <circle cx="150" cy="150" r="140" fill="none" stroke="var(--faint)" stroke-width="14"/>
    </svg>

    <div class="brand-lockup">
      <svg width="64" height="64" viewBox="0 0 64 64" aria-hidden="true">
        <circle cx="32" cy="32" r="30" fill="var(--brand-green)"/>
      </svg>
      <span class="brand-name">ARC VOLLEY</span>
    </div>

    <div class="person">
      <p class="person-name">박 서 윤</p>
      <p class="person-title">대표</p>
    </div>
    <div class="divider"></div>
    <ul class="contact-list">
      <li class="contact-item">
        <svg viewBox="0 0 16 16" aria-hidden="true"><path d="M2 5c0-2 3-3 6-3s6 1 6 3v1h-3V5H5v1H2zM3 8h10l1 6H2z"/></svg>
        010-8472-3916
      </li>
      <li class="contact-item">
        <svg viewBox="0 0 16 16" aria-hidden="true"><path d="M1 4h14v1L8 9 1 5zM1 6.5l7 4 7-4V12H1z"/></svg>
        seoyun.park@arcvolley-example.co.kr
      </li>
      <li class="contact-item">
        <svg viewBox="0 0 16 16" aria-hidden="true"><path d="M8 1a7 7 0 1 0 0 14A7 7 0 0 0 8 1zm0 1.6a5.4 5.4 0 1 1 0 10.8A5.4 5.4 0 0 1 8 2.6zM2.5 7.3h11v1.4h-11z"/></svg>
        www.arcvolley-example.co.kr
      </li>
      <li class="contact-item">
        <svg viewBox="0 0 16 16" aria-hidden="true"><path d="M2 2h12v12H2zM3.6 3.6v8.8h8.8V3.6z"/></svg>
        arcvolley
      </li>
      <li class="contact-item address">
        <svg viewBox="0 0 16 16" aria-hidden="true"><path d="M8 1a5 5 0 0 0-5 5c0 4 5 9 5 9s5-5 5-9a5 5 0 0 0-5-5zm0 3a2 2 0 1 1 0 4 2 2 0 0 1 0-4z"/></svg>
        경기도 용인시 수지구 풍덕천로 456 미래타워 5층 501호, 502호
      </li>
    </ul>
  </section>

  <section class="card card-back">
    <div class="back-lockup">
      <svg width="150" height="150" viewBox="0 0 150 150" aria-hidden="true">
        <circle cx="75" cy="75" r="70" fill="none" stroke="var(--card-white)" stroke-width="8"/>
      </svg>
      <span class="brand-name">ARC VOLLEY</span>
    </div>
  </section>
</body>
</html>
```